Website R86 coffee

I am opening a small business selling locally roasted coffee online. To start with I want a site with three pages. 1. A welcome page with logo and mission/vision. 2. Shopping/ordering page. 3. About Us page. The brand is "R86 Coffee - A warm start to every day". We are giving back to the downs syndrome community by employing people with down syndrome (Trisomy 21) and buy donating to down syndrome research.

Target Market(s)

Families and friends of people with downs syndrome

Coding

Coded - Design and coding required

Number of Pages Required

3 page

```html
<!DOCTYPE html>
<html lang="en">
<head>
<meta charset="utf-8">
<title>R86 Coffee</title>
<link href="https://fonts.googleapis.com/css2?family=Questrial&family=Lato:wght@400;700&display=swap" rel="stylesheet">
<style>
:root{
  --accent:#c2452a;
  --ink:#2b2b2b;
  --muted:#5a5a5a;
  --white:#ffffff;
  --line:#dcdcdc;
  --footer-a:#161616;
  --footer-b:#3a3a3a;
}
*{box-sizing:border-box;margin:0;padding:0}
html,body{width:1200px;height:4219px;overflow:hidden}
body{position:relative;background:var(--white);font-family:'Lato',sans-serif;color:var(--ink)}
.abs{position:absolute}
.heading{font-family:'Questrial',sans-serif;font-weight:400;letter-spacing:1px}
.rule{position:absolute;height:3px;width:65px;background:var(--accent)}
.btn{position:absolute;background:var(--accent);color:var(--white);font-family:'Lato',sans-serif;font-weight:700;font-size:13.5px;display:flex;align-items:center;justify-content:center;text-transform:uppercase}
.photo{position:absolute}
.topbar{left:0;top:0;width:1200px;height:31px;background:var(--accent);color:var(--white);font-size:13.5px;font-weight:700;letter-spacing:1px;display:flex;align-items:center;justify-content:center}
.account-icon{position:absolute;right:158px;top:4px}
.brand{left:157px;top:58px;font-family:'Questrial',sans-serif;font-size:30px;color:var(--ink);letter-spacing:1px}
.nav a{position:absolute;top:78px;font-size:13.5px;color:var(--ink);text-decoration:none;text-transform:uppercase}
.nav a.active{color:var(--accent)}
.hero{left:0;top:141px;width:1200px;height:496px;background:linear-gradient(100deg,#2e1a10 0%,#5a3524 35%,#7a4a30 60%,#4a2a18 100%)}
.hero-title{left:149px;top:286px;font-size:43px;color:var(--white);letter-spacing:4px}
.hero-text{left:157px;top:348px;width:420px;font-size:15px;line-height:23.5px;color:var(--white)}
.frame{position:absolute;border:2px solid #1a1a1a}
.shadow{box-shadow:0 0 8px rgba(0,0,0,.25)}
.sec-title{position:absolute;font-size:31px;color:var(--ink)}
.sec-text{position:absolute;font-size:13px;line-height:22.3px;color:var(--muted)}
.band{left:0;top:1822px;width:1200px;height:372px;background:linear-gradient(90deg,#8a3a22,#b24e2e 50%,#9a4124)}
.band-title{left:0;width:1200px;top:1908px;text-align:center;font-size:36px;color:var(--white)}
.band-text{left:0;width:1200px;top:1960px;text-align:center;font-size:23px;line-height:36px;color:var(--white)}
.grid{left:0;top:2881px;width:1200px;height:575px;display:grid;grid-template-columns:repeat(4,300px);grid-template-rows:repeat(2,287.5px)}
.grid div{width:300px;height:287.5px}
.mail-input{left:372px;top:3620px;width:458px;height:45px;background:#f1f1f1;border:1px solid var(--line);font-size:13.5px;font-weight:700;display:flex;align-items:center;justify-content:center;color:var(--ink)}
.footer{left:0;top:3826px;width:1200px;height:393px;background:linear-gradient(100deg,var(--footer-a),var(--footer-b));color:var(--white)}
.footer .brand-foot{position:absolute;left:159px;top:92px;font-family:'Questrial',sans-serif;font-size:27px;letter-spacing:1px}
.footer .col-title{position:absolute;top:109px;font-size:15px}
.footer .col-rule{position:absolute;top:141px;width:34px;height:2px;background:var(--accent)}
.footer .link{position:absolute;font-size:12.5px;color:#e6e6e6}
.footer .contact{position:absolute;left:157px;font-size:13.5px;display:flex;align-items:center;gap:10px}
.footer .dot{position:absolute;width:11px;height:11px;border-radius:50%;background:#e6e6e6}
.copyright{position:absolute;left:0;width:1200px;top:314px;text-align:center;font-size:13px;color:#e6e6e6}
.copyright span{color:var(--accent)}
</style>
</head>
<body>

<div class="abs topbar">FREE SHIPPING ON ALL ORDER
  <svg class="account-icon" width="24" height="24" viewBox="0 0 24 24"><circle cx="12" cy="12" r="11" fill="none" stroke="#fff" stroke-width="2"/><circle cx="12" cy="9" r="3.5" fill="#fff"/><path d="M5.5 18.5c1.5-3 4-4 6.5-4s5 1 6.5 4" fill="#fff"/></svg>
</div>

<header>
  <div class="abs brand">R86 COFFEE</div>
  <nav class="nav">
    <a class="active" style="left:627px">Home</a>
    <a style="left:712px">Shopping</a>
    <a style="left:828px">Order</a>
  </nav>
  <div class="btn" style="left:908px;top:65px;width:135px;height:43px">Donate Now</div>
</header>

<section>
  <div class="abs hero" role="img" aria-label="Cup of coffee with heart-shaped steam beside roasted beans on a wooden table"></div>
  <h1 class="abs heading hero-title">R 86 COFFEE</h1>
  <p class="abs hero-text">Many desktop publishing packages and web page editors now use Lorem Ipsum as their default model text, and a search for 'lorem ipsum' will uncover</p>
  <div class="btn" style="left:159px;top:444px;width:132px;height:45px">Buy Now</div>
</section>

<section>
  <div class="photo shadow" style="left:157px;top:751px;width:432px;height:416px;background:linear-gradient(120deg,#c77a55,#a3482c 55%,#e8d8cc)" role="img" aria-label="Two friends laughing while sharing cups of coffee"></div>
  <div class="frame" style="left:177px;top:740px;width:394px;height:437px"></div>
  <h2 class="heading sec-title" style="left:683px;top:890px">VISION</h2>
  <div class="rule" style="left:683px;top:935px"></div>
  <p class="sec-text" style="left:683px;top:956px;width:350px">Develop A Company That Markets Coffee And Related Products To Family And Friends Of The Down Syndrome Community</p>
</section>

<section>
  <h2 class="heading sec-title" style="left:155px;top:1377px">MISSION</h2>
  <div class="rule" style="left:155px;top:1423px"></div>
  <p class="sec-text" style="left:157px;top:1440px;width:385px">Create And Grow An Online Company Selling Contract Roasted Coffee. As Growth Permits Become A Fully Vertically Integrated Coffee Company From Roasting To Our Own Coffee Shop. The Company Will Give Significant Funds To Medical Research In Downs Syndrome And We Will Hire As Many People With Downs Syndrome As Possible.</p>
  <div class="photo shadow" style="left:611px;top:1287px;width:427px;height:416px;background:radial-gradient(circle at 50% 45%,#2a160c 0,#3e2214 35%,#7a3e24 70%,#93502e 100%)" role="img" aria-label="Bowl of roasted coffee beans with a wooden scoop on a dark table"></div>
  <div class="frame" style="left:629px;top:1277px;width:394px;height:437px"></div>
</section>

<section>
  <div class="abs band" role="img" aria-label="Smiling team members working together in a bright café"></div>
  <h2 class="abs heading band-title">R86 Coffee</h2>
  <p class="abs band-text">A warm start to every day . We are giving back to the downs syndrome<br>community by employing people with down syndrome</p>
  <div class="btn" style="left:534px;top:2053px;width:134px;height:44px">Buy Now</div>
</section>

<section>
  <div class="photo shadow" style="left:164px;top:2274px;width:348px;height:412px;background:linear-gradient(160deg,#a98a70,#6e4a34 40%,#c9b39c 70%,#5a3a28)" role="img" aria-label="Burlap sacks filled with roasted coffee beans"></div>
  <h2 class="heading sec-title" style="left:607px;top:2357px">SHOP NOW</h2>
  <div class="rule" style="left:607px;top:2399px"></div>
  <p class="sec-text" style="left:607px;top:2420px;width:425px">If you are going to use a passage of Lorem Ipsum, you need to be sure there isn't anything embarrassing hidden in the middle of text. All the Lorem Ipsum generators on the Internet tend to repeat predefined chunks as necessary, making this the first true generator on the Internet.</p>
  <div class="btn" style="left:607px;top:2550px;width:135px;height:46px">Buy Now</div>
</section>

<section>
  <h2 class="abs heading sec-title" style="left:0;width:1200px;text-align:center;top:2794px">GET INSPIRED</h2>
  <div class="rule" style="left:567px;top:2838px"></div>
  <div class="abs grid">
    <div style="background:linear-gradient(135deg,#5a3020,#2a160c)" role="img" aria-label="Coffee beans with a wooden scoop"></div>
    <div style="background:linear-gradient(135deg,#c9a080,#7a4a34)" role="img" aria-label="Woman smiling with a cup of coffee"></div>
    <div style="background:linear-gradient(180deg,#6a5a48,#2e3a48)" role="img" aria-label="Blue enamel mug outdoors"></div>
    <div style="background:linear-gradient(135deg,#e6e2dc,#b8b0a6)" role="img" aria-label="Steaming cup of coffee on a saucer"></div>
    <div style="background:linear-gradient(135deg,#2a2420,#6a4a30)" role="img" aria-label="Paper coffee bag and pouch"></div>
    <div style="background:linear-gradient(135deg,#3a3a3a,#1e1410)" role="img" aria-label="Glasses of layered coffee drinks"></div>
    <div style="background:linear-gradient(135deg,#b8703e,#5a2e1a)" role="img" aria-label="Friends chatting over coffee at a café table"></div>
    <div style="background:linear-gradient(135deg,#8a7a6a,#4a3020)" role="img" aria-label="Sacks of coffee beans"></div>
  </div>
</section>

<section>
  <div class="photo" style="left:101px;top:3593px;width:325px;height:172px;background:radial-gradient(ellipse at 35% 45%,#2a1a12 0,#6a4a38 35%,#f3f0ec 70%,#ffffff 100%)" role="img" aria-label="Cup of espresso on a saucer with scattered beans"></div>
  <div class="photo" style="left:859px;top:3503px;width:225px;height:292px;background:radial-gradient(ellipse at 50% 50%,#b08060 0,#d8c0a8 40%,#ffffff 75%)" role="img" aria-label="Iced coffee in a tall glass with a striped straw"></div>
  <h2 class="abs heading sec-title" style="left:0;width:1200px;text-align:center;top:3538px">NEWSLETTER</h2>
  <div class="rule" style="left:567px;top:3581px"></div>
  <div class="abs mail-input">ENTER YOUR MAIL ID</div>
  <div class="btn" style="left:534px;top:3680px;width:134px;height:46px">Submit</div>
</section>

<footer class="abs footer">
  <div class="brand-foot">R86 COFFEE</div>
  <div class="contact" style="top:165px">
    <svg width="13" height="13" viewBox="0 0 24 24"><path fill="#fff" d="M6.6 10.8c1.4 2.8 3.8 5.1 6.6 6.6l2.2-2.2c.3-.3.7-.4 1-.2 1.1.4 2.3.6 3.6.6.6 0 1 .4 1 1V20c0 .6-.4 1-1 1C10.6 21 3 13.4 3 4c0-.6.4-1 1-1h3.5c.6 0 1 .4 1 1 0 1.3.2 2.5.6 3.6.1.3 0 .7-.2 1z"/></svg>
    555-018-2046</div>
  <div class="contact" style="top:201px">
    <svg width="13" height="15" viewBox="0 0 24 28"><path fill="#fff" d="M12 0C7 0 3 4 3 9c0 7 9 19 9 19s9-12 9-19c0-5-4-9-9-9zm0 13a4 4 0 110-8 4 4 0 010 8z"/></svg>
    12 Roastery Lane, pin 560-218</div>
  <div class="contact" style="top:237px">
    <svg width="13" height="10" viewBox="0 0 24 18"><rect width="24" height="18" fill="#fff"/><path d="M0 0l12 10L24 0" fill="none" stroke="#222" stroke-width="2"/></svg>
    hello@r86coffee.example</div>

  <div class="col-title" style="left:458px">Quick Link</div>
  <div class="col-rule" style="left:458px"></div>
  <div class="link" style="left:458px;top:165px">Home</div>
  <div class="link" style="left:458px;top:198px">Shopping</div>
  <div class="link" style="left:458px;top:231px">Order</div>

  <div class="col-title" style="left:630px">Shopping</div>
  <div class="col-rule" style="left:630px"></div>
  <div class="link" style="left:630px;top:167px">loremipsum</div>
  <div class="link" style="left:630px;top:200px">loremipsum</div>
  <div class="link" style="left:630px;top:233px">loremipsum</div>

  <div class="col-title" style="left:787px">Information</div>
  <div class="col-rule" style="left:787px"></div>
  <div class="link" style="left:787px;top:165px">Log in</div>
  <div class="link" style="left:787px;top:198px">My Account</div>
  <div class="link" style="left:787px;top:231px">Order Detais</div>

  <div class="col-title" style="left:949px">Social</div>
  <div class="col-rule" style="left:949px"></div>
  <div class="dot" style="left:954px;top:167px"></div><div class="link" style="left:987px;top:165px">Circleline</div>
  <div class="dot" style="left:954px;top:197px"></div><div class="link" style="left:987px;top:195px">Chirpnet</div>
  <div class="dot" style="left:954px;top:226px"></div><div class="link" style="left:987px;top:224px">Snapframe</div>
  <div class="dot" style="left:954px;top:256px"></div><div class="link" style="left:987px;top:254px">Workweb</div>

  <div class="copyright">© 2021 <span>r86coffee</span>. All rights reserved.</div>
</footer>

</body>
</html>
```